Fiber Optic Internet flyer promotion Winter 2016-2017

I am looking for a marketing flyer that will not be folded, single sided that will advertise a Fiber Optic internet promotion that we are currently running.

The design should be clean, flow well, quickly grab attention, and if a very few short seconds list what the promotion is, and direct them to contact us.

It needs to list a few features of the promotion, but does not need to be in this order and should flow well with the flyer
1.) Fiber Optic Internet
2.) 100 Mbits for $140 /month or 150 Mbits for $190 /month
3.) Free construction cost up to $10,000, limited funds available.
4.) Limited time offer. Must commit before funds run out.

(555) 274-3916, www.kelvoranet.example

Target Market(s)

Small to large business

Industry/Entity Type

Internet Service Provider

Requirements
Must have
• Eye catching appeal. Quickly convey the message of the promotion and our company name and phone number.
Should not have
• Our company is primarily a wireless ISP. This promotion is all about Fiber Optic. I do not want to draw attention to the "wireless" portion of our business with this flyer.

```html
<!DOCTYPE html>
<html lang="en">
<head>
<meta charset="utf-8">
<title>Fiber Optic Internet – Kelvora Net</title>
<link rel="stylesheet" href="https://fonts.googleapis.com/css2?family=Exo+2:ital,wght@1,800&family=Oswald:wght@400;500;600&family=Montserrat:wght@500;700&display=swap">
<style>
  :root {
    --red: #e3243b;
    --red-soft: #f15b6c;
    --red-bar: #cf2636;
    --navy: #0f2b7a;
    --ink: #111111;
    --white: #ffffff;
    --space-deep: #02060f;
    --space-blue: #0b3f7d;
    --glow: #39a6ff;
  }
  * { margin: 0; padding: 0; box-sizing: border-box; }
  html, body { width: 928px; height: 1200px; overflow: hidden; background: var(--white); }
  .flyer { position: relative; width: 928px; height: 1200px; overflow: hidden; background: var(--white); }

  .hero {
    position: absolute; left: 0; top: 0; width: 928px; height: 574px;
    background:
      radial-gradient(ellipse 75% 55% at 55% 68%, rgba(57,166,255,.55) 0%, rgba(11,63,125,.6) 45%, rgba(2,6,15,0) 75%),
      linear-gradient(180deg, var(--space-deep) 0%, #041226 45%, var(--space-blue) 100%);
  }
  .headline {
    position: absolute; left: 0; top: 28px; width: 928px; text-align: center;
    font-family: "Exo 2", sans-serif; font-style: italic; font-weight: 800;
    font-size: 56px; letter-spacing: 3px; color: var(--white);
  }

  .price-band {
    position: absolute; left: 0; width: 644px; height: 78px;
    border-radius: 0 39px 39px 0;
    display: flex; align-items: center; padding-left: 18px;
    font-family: "Oswald", sans-serif; color: var(--white); white-space: nowrap;
  }
  .price-band--basic { top: 593px; background: var(--red); }
  .price-band--plus { top: 687px; background: var(--red-soft); }
  .price-speed { font-size: 74px; font-weight: 600; line-height: 1; margin-right: 14px; letter-spacing: -1px; }
  .price-detail { font-size: 38px; font-weight: 400; line-height: 1; padding-top: 14px; }
  .price-amount { font-weight: 600; font-size: 46px; }
  .price-or { font-size: 28px; }

  .offer-title {
    position: absolute; left: 26px; top: 806px;
    font-family: "Oswald", sans-serif; font-weight: 600; font-size: 66px;
    color: var(--red); line-height: 1;
  }
  .offer-note {
    position: absolute; left: 28px; top: 884px;
    font-family: "Oswald", sans-serif; font-weight: 500; font-size: 33px;
    color: var(--ink); line-height: 1;
  }
  .offer-terms {
    position: absolute; left: 28px; top: 954px;
    font-family: "Montserrat", sans-serif; font-weight: 500; font-size: 20px;
    color: var(--ink); line-height: 33px; word-spacing: 6px; letter-spacing: .5px;
  }
  .call-to-action {
    position: absolute; left: 28px; top: 1060px;
    font-family: "Montserrat", sans-serif; font-weight: 700; font-size: 26px;
    color: var(--red);
  }

  .brand {
    position: absolute; left: 598px; top: 1000px; width: 300px;
    display: flex; align-items: center; gap: 12px;
    font-family: "Montserrat", sans-serif; font-weight: 700; font-size: 30px;
    color: var(--navy); letter-spacing: 1px;
  }
  .brand-dot { width: 22px; height: 22px; border-radius: 50%; background: var(--navy); flex: none; }

  .contact-bar {
    position: absolute; left: 0; top: 1108px; width: 928px; height: 92px;
    background: var(--red-bar);
    display: flex; align-items: center; padding-left: 26px; gap: 44px;
    font-family: "Montserrat", sans-serif; font-weight: 700; font-size: 24px;
    color: var(--white); letter-spacing: 2px;
  }
  .contact-item { display: flex; align-items: center; gap: 14px; }
  .contact-item svg { fill: var(--white); flex: none; }
</style>
</head>
<body>
<div class="flyer">
  <div class="hero" role="img" aria-label="Glowing blue globe wrapped in a network of light trails against a starry night sky"></div>
  <h1 class="headline">FIBER OPTIC INTERNET!</h1>

  <div class="price-band price-band--basic">
    <span class="price-speed">100 MB</span>
    <span class="price-detail">FOR <span class="price-amount">$140</span>/MONTH <span class="price-or">OR</span></span>
  </div>
  <div class="price-band price-band--plus">
    <span class="price-speed">150 MB</span>
    <span class="price-detail">FOR <span class="price-amount">$190</span> / MONTH</span>
  </div>

  <h2 class="offer-title">LIMITED TIME OFFER!</h2>
  <p class="offer-note">MUST COMMIT BEFORE FUNDS RUN OUT</p>
  <p class="offer-terms">FREE CONSTRUCTION COST UP TO $10,000<br>LIMITED FUNDS AVAILABLE.</p>
  <p class="call-to-action">HURRY UP &amp; CONTACT US!</p>

  <div class="brand"><span class="brand-dot"></span><span>KELVORA NET</span></div>

  <div class="contact-bar">
    <div class="contact-item">
      <svg width="22" height="22" viewBox="0 0 24 24" aria-hidden="true"><path d="M6.6 10.8c1.4 2.8 3.8 5.1 6.6 6.6l2.2-2.2c.3-.3.7-.4 1-.2 1.1.4 2.3.6 3.6.6.6 0 1 .4 1 1V20c0 .6-.4 1-1 1C10.6 21 3 13.4 3 4c0-.6.4-1 1-1h3.5c.6 0 1 .4 1 1 0 1.3.2 2.5.6 3.6.1.3 0 .7-.2 1l-2.3 2.2z"/></svg>
      <span>(555) 274-3916</span>
    </div>
    <div class="contact-item">
      <svg width="28" height="26" viewBox="0 0 28 26" aria-hidden="true"><path d="M2 2h24v16H2z M4 4v12h20V4z M11 20h6v2h3v2H8v-2h3z" fill-rule="evenodd"/></svg>
      <span>WWW.KELVORANET.EXAMPLE</span>
    </div>
  </div>
</div>
</body>
</html>
```